Velmora Supply Chain and Logistic Consulting

Please review the attached Business Card. I want as close to this card with the colors, fonts, and quality of the card as possible. The attached compass should replace the deer head on both sides of the card and the text should say:

Backside
Compass JPEG
Velmora SC&L
A Supply Chain and Logistics Consulting Company

Frontside
Velmora SC&L
Ravi Ostrander - Tampa Florida
President
____________________________________
(727) 555-0193
VelmoraSCL@Quillpost.com
_____________________________________

Bottom Front Side

Target Market(s)

Businesses

Contact Information for Business Card

Backside
Compass JPEG
Velmora SC&L

Frontside
Velmora SC&L
President
(727) 555-0193
VelmoraSCL@Quillpost.com

Bottom Front Side

Font styles to use
Serif
Script

Colors

Designer to choose colors to be used in the design.

Requirements
Must have
• See attached card for reference
Nice to have
Should not have

```html
<!DOCTYPE html>
<html lang="en">
<head>
<meta charset="utf-8">
<title>Velmora SC&amp;L Business Card</title>
<link rel="stylesheet" href="https://fonts.googleapis.com/css2?family=Cinzel:wght@400&family=Cormorant+SC:wght@500&family=Tinos:wght@400;700&display=swap">
<style>
  :root {
    --backdrop: #3a3a3a;
    --card: #262626;
    --card-edge: #1c1c1c;
    --ink: #f2f2f2;
    --ink-soft: #d9d9d9;
    --rule: #9a9a9a;
    --accent: #3d5a80;
  }
  * { margin: 0; padding: 0; box-sizing: border-box; }
  html, body {
    width: 1200px;
    height: 1021px;
    overflow: hidden;
    background: var(--backdrop);
  }
  .stage {
    width: 1200px;
    height: 1021px;
    display: flex;
    flex-direction: column;
    align-items: center;
    justify-content: center;
    gap: 60px;
  }
  .card {
    width: 760px;
    height: 434px;
    background: linear-gradient(160deg, #2c2c2c 0%, var(--card) 60%, var(--card-edge) 100%);
    box-shadow: 0 18px 40px rgba(0,0,0,0.45);
    position: relative;
    color: var(--ink);
    text-align: center;
  }
  /* Back side */
  .card-back {
    display: flex;
    flex-direction: column;
    align-items: center;
    justify-content: center;
  }
  .brand-dot {
    width: 150px;
    height: 150px;
    border-radius: 50%;
    background: var(--accent);
    margin-bottom: 30px;
  }
  .wordmark {
    font-family: "Cinzel", serif;
    font-weight: 400;
    font-size: 44px;
    letter-spacing: 3px;
    line-height: 1;
    color: var(--ink);
    white-space: nowrap;
  }
  /* Front side */
  .card-front {
    padding-top: 60px;
  }
  .card-front .wordmark { font-size: 40px; }
  .contact-name {
    font-family: "Tinos", serif;
    font-weight: 700;
    font-size: 21px;
    margin-top: 26px;
  }
  .contact-role {
    font-family: "Tinos", serif;
    font-size: 18px;
    color: var(--ink-soft);
    margin-top: 2px;
  }
  .rule {
    width: 440px;
    height: 1px;
    margin: 12px auto;
    background: linear-gradient(90deg, transparent, var(--rule) 20%, var(--rule) 80%, transparent);
  }
  .contact-line {
    font-family: "Tinos", serif;
    font-size: 20px;
    letter-spacing: 1px;
    line-height: 1.3;
  }
  .tagline {
    position: absolute;
    left: 0;
    right: 0;
    bottom: 44px;
    display: flex;
    align-items: center;
    justify-content: center;
    gap: 14px;
    font-family: "Cormorant SC", serif;
    font-weight: 500;
    font-size: 22px;
    letter-spacing: 1.5px;
    color: var(--ink-soft);
  }
  .tagline::before, .tagline::after {
    content: "";
    width: 60px;
    height: 1px;
    background: var(--rule);
  }
</style>
</head>
<body>
  <main class="stage">
    <section class="card card-back" aria-label="Card back">
      <div class="brand-dot"></div>
      <div class="wordmark">Velmora SC&amp;L</div>
    </section>

    <section class="card card-front" aria-label="Card front">
      <div class="wordmark">Velmora SC&amp;L</div>
      <p class="contact-name">Ravi Ostrander - Tampa Florida</p>
      <p class="contact-role">President</p>
      <div class="rule"></div>
      <p class="contact-line">727-555-0193</p>
      <p class="contact-line">VelmoraSCL@Quillpost.com</p>
      <div class="rule"></div>
      <p class="tagline">A Supply Chain and Logistics Consulting Company</p>
    </section>
  </main>
</body>
</html>
```